Mobile Friendly Lead Generation Landing Page

We are a web marketing company that specialized in web lead generation. Recently we have started buying media from mobile devices and we need a mobile interface(landing page) where we can collect user data in an effective manner.

Our current mobile landing page is:
http://www.pathwaylocate.example.com/lp13d/index.aspx?a=true&source=591483
Through this you can see what the steps/questions users need to answer to get matched to a school. We need the design for the whole process.

We are pretty open for design ideas and our goal is to make this mobile optimized landing page have the look and feel of an app...but not an app.
There are several questions in the process but we are open to changing the way they are presented. As in, you can have one question at a time or a few.
The goal is to make this EXTREMELY EASY for users to interact with.

One example that we have liked is:
http://tutorhubnet.example.com/schools/72615-page1.thub (please note that this opens only on mobile devices)

Some of these screenshots are attached.

Our web form looks like this:
http://www.pathwaylocate.example.com/lp88/index.aspx?a=true

```html
<!DOCTYPE html>
<html lang="en">
<head>
<meta charset="utf-8">
<title>School Match – Contact Details</title>
<link rel="stylesheet" href="https://fonts.googleapis.com/css2?family=Montserrat:wght@400;500;600;700&display=swap">
<style>
  :root {
    --page-bg: #eeeeee;
    --brand-green: #84b500;
    --field-bg: #ffffff;
    --label-ink: #3a3a3a;
    --body-ink: #2e3a10;
    --white: #ffffff;
    --button-top: #ffffff;
    --button-bottom: #dcdcdc;
    --divider: #d6d6d6;
  }
  * { box-sizing: border-box; margin: 0; padding: 0; }
  html, body {
    width: 1200px; height: 900px; overflow: hidden;
    background: var(--page-bg);
    font-family: "Montserrat", Arial, sans-serif;
  }
  .screen {
    position: absolute; left: 354px; top: 14px;
    width: 351px; height: 623px;
    background: var(--brand-green);
    transform: scale(1.4); transform-origin: top left;
    overflow: hidden;
  }
  .field {
    position: absolute; left: 16px; width: 320px; height: 41px;
    background: var(--field-bg);
    display: flex; align-items: center;
  }
  .field-required {
    position: absolute; left: 6px; top: 1px;
    font-size: 8px; color: var(--label-ink); line-height: 1;
  }
  .field-label {
    width: 93px; padding-left: 18px;
    font-size: 11px; font-weight: 600; color: var(--label-ink);
    border-right: 2px solid var(--divider); line-height: 22px;
  }
  .field-input { flex: 1; height: 100%; }
  .field--last-name { top: -4px; }
  .field--email { top: 60px; }
  .field--phone { top: 121px; }
  .field--zip { top: 182px; }
  .field--address { top: 244px; left: 17px; }
  .form-note {
    position: absolute; top: 318px; left: 0; width: 100%;
    text-align: center; font-size: 8.5px; font-weight: 700; color: var(--white);
  }
  .next-button {
    position: absolute; left: 71px; top: 359px; width: 210px; height: 60px;
    border-radius: 5px;
    background: linear-gradient(var(--button-top) 45%, var(--button-bottom));
    box-shadow: 0 2px 3px rgba(0,0,0,0.25);
    display: flex; align-items: center; justify-content: center;
    font-size: 29px; font-weight: 700; color: var(--brand-green); letter-spacing: 0.5px;
  }
  .secure-badge {
    position: absolute; left: 22px; top: 474px;
    display: flex; align-items: flex-end; gap: 8px;
  }
  .secure-title { font-size: 8.5px; font-weight: 600; color: var(--body-ink); margin-bottom: 2px; }
  .secure-text {
    position: absolute; left: 23px; top: 524px; width: 280px;
    font-size: 6.2px; font-weight: 600; line-height: 10.5px; color: var(--body-ink);
  }
  .site-footer {
    position: absolute; left: 22px; top: 591px;
    font-size: 5.2px; font-weight: 700; color: var(--body-ink); white-space: nowrap;
  }
</style>
</head>
<body>
  <main class="screen">
    <form class="lead-form">
      <div class="field field--last-name"><span class="field-required">*</span><span class="field-label">Last Name</span><span class="field-input"></span></div>
      <div class="field field--email"><span class="field-required">*</span><span class="field-label">Email</span><span class="field-input"></span></div>
      <div class="field field--phone"><span class="field-required">*</span><span class="field-label">Phone</span><span class="field-input"></span></div>
      <div class="field field--zip"><span class="field-required">*</span><span class="field-label">Zip code</span><span class="field-input"></span></div>
      <div class="field field--address"><span class="field-required">*</span><span class="field-label">Address</span><span class="field-input"></span></div>
      <p class="form-note">Please fil in the fields marked with *</p>
      <div class="next-button">NEXT</div>
    </form>
    <div class="secure-badge">
      <svg width="31" height="36" viewBox="0 0 31 36" aria-hidden="true">
        <path d="M9 11 V7 a6.5 6.5 0 0 1 13 0 V11" fill="none" stroke="#fff" stroke-width="2.5"/>
        <rect x="0" y="11" width="31" height="19" fill="#fff"/>
        <rect x="0" y="32" width="31" height="3" fill="#fff"/>
      </svg>
      <span class="secure-title">Your information is secure</span>
    </div>
    <p class="secure-text">Your information allows us to connect you with schols that match based on your interests. You will only recieve information from the schools you choose, info such as courses, tution, financial aid, etc</p>
    <footer class="site-footer">Copyright @ PathwayLocate.example.com | All Rights Reserved. Privacy Policy | Unsubscribe | Advertising with us</footer>
  </main>
</body>
</html>
```